Luggage and travel essentials company needs Letterhead design (including logo)

Brambury luggage is a travel retailer focussed on selling luggage and travel essentials.
We are a company that have a traditional approach to customer service and also embraces the latest technology, especially where it improves the customer experience.
I would like the design to have an airport hint (airport imagery and font preferred), I would also like the colour blue to feature heavily (see attached image for colour hint).
The final design should aim to give the customer confidence that we are dependable and reliable (no script fonts or crazy colours please) but also reflect that we are an innovative and technology focused company.
I would like the letterhead design to include a logo and text.
I am interested in letterhead text containing an embedded logo (much like the 'Z' in Zephyra's logo is also used separately) Note: this is optional.
The text of the letterhead should include the words "Brambury Luggage & Travel Essentials", and should include a space for the company phone number, email address, website address along with the company physical address.
Target Market(s)
Affluent Adults aged 25 years and above - Predominantly female
Industry/Entity Type
Airport

```html
<!DOCTYPE html>
<html lang="en">
<head>
<meta charset="utf-8">
<title>Brambury Luggage &amp; Travel Essentials – Letterhead</title>
<link rel="stylesheet" href="https://fonts.googleapis.com/css2?family=Montserrat:wght@700&family=Open+Sans:wght@300;400&display=swap">
<style>
  :root {
    --backdrop: #e8e9eb;
    --paper: #f7f7f8;
    --ink: #3b3f46;
    --ink-soft: #6c7078;
    --blue: #2a8fc4;
    --blue-light: #8cc3dc;
    --rule: #c9ccd1;
    --watermark: #eeeff1;
  }
  * { box-sizing: border-box; margin: 0; padding: 0; }
  html, body {
    width: 1200px; height: 936px; overflow: hidden;
    background: var(--backdrop);
  }
  .letterhead {
    position: absolute; left: 296px; top: 38px;
    width: 608px; height: 860px;
    background: var(--paper);
    box-shadow: 0 10px 30px rgba(0,0,0,.12);
    overflow: hidden;
  }
  .watermark {
    position: absolute; left: 250px; top: -40px;
    width: 130px; height: 130px; border-radius: 50%;
    background: var(--watermark);
  }
  .brand {
    position: absolute; left: 54px; top: 70px;
    display: flex; align-items: center; gap: 8px;
  }
  .brand-name {
    font-family: 'Montserrat', sans-serif; font-weight: 700;
    font-size: 21px; letter-spacing: 1px; color: var(--ink);
  }
  .brand-dot {
    width: 18px; height: 18px; border-radius: 50%;
    background: var(--blue);
  }
  .brand-tagline {
    font-family: 'Open Sans', sans-serif; font-weight: 400;
    font-size: 11px; line-height: 1.2; color: var(--ink-soft);
    margin-left: 2px;
  }
  .contact {
    position: absolute; left: 54px; right: 54px; bottom: 44px;
    display: flex; align-items: center; gap: 22px;
    font-family: 'Open Sans', sans-serif; font-weight: 400;
    font-size: 8.5px; line-height: 1.55; color: var(--ink-soft);
  }
  .contact-group { display: flex; flex-direction: column; }
  .contact-divider { width: 1px; height: 26px; background: var(--rule); }
  .contact-line { display: flex; align-items: center; gap: 5px; }
  .contact-icon {
    width: 10px; height: 10px; border-radius: 2px;
    background: var(--blue); display: flex; align-items: center; justify-content: center;
  }
  .contact-icon svg { width: 7px; height: 7px; }
  .footer-band {
    position: absolute; left: 0; right: 0; bottom: 14px;
    height: 7px; background: var(--blue);
  }
  .footer-band-accent {
    position: absolute; right: 0; bottom: 14px;
    width: 80px; height: 16px; background: var(--blue-light);
    border-left: 3px solid var(--paper);
  }
</style>
</head>
<body>
  <main class="letterhead">
    <div class="watermark" aria-hidden="true"></div>

    <header class="brand">
      <span class="brand-name">BRAMBURY</span>
      <span class="brand-dot" aria-hidden="true"></span>
      <span class="brand-tagline">Luggage &amp;<br>Travel Essentials</span>
    </header>

    <footer class="contact">
      <div class="contact-group">
        <span>2417 Harbour Lane</span>
        <span>Westfield, FL 34120</span>
      </div>
      <span class="contact-divider"></span>
      <div class="contact-group">
        <span class="contact-line">
          <span class="contact-icon"><svg viewBox="0 0 10 10"><path d="M2 1h2l1 2.5-1.3 1a6 6 0 0 0 2.8 2.8l1-1.3L10 7v2a1 1 0 0 1-1 1A9 9 0 0 1 0 1a1 1 0 0 1 1-1z" fill="#fff"/></svg></span>
          (02) 5550-1846
        </span>
        <span class="contact-line">
          <span class="contact-icon"><svg viewBox="0 0 10 10"><rect x="1" y="3" width="8" height="5" fill="#fff"/><rect x="3" y="1" width="4" height="2" fill="#fff"/></svg></span>
          (02) 5550-2937
        </span>
      </div>
      <span class="contact-divider"></span>
      <div class="contact-group">
        <span class="contact-line">
          <span class="contact-icon"><svg viewBox="0 0 10 10"><circle cx="5" cy="5" r="4" fill="none" stroke="#fff" stroke-width="1.2"/><path d="M1 5h8M5 1v8" stroke="#fff" stroke-width="0.9"/></svg></span>
          www.bramburyluggage.com
        </span>
        <span class="contact-line">
          <span class="contact-icon"><svg viewBox="0 0 10 10"><rect x="1" y="2" width="8" height="6" fill="none" stroke="#fff" stroke-width="1.1"/><path d="M1 2l4 3.5L9 2" fill="none" stroke="#fff" stroke-width="1.1"/></svg></span>
          info@bramburyluggage.com
        </span>
      </div>
    </footer>

    <div class="footer-band" aria-hidden="true"></div>
    <div class="footer-band-accent" aria-hidden="true"></div>
  </main>
</body>
</html>
```